New Vegan Documentary Film Needs Poster Design

We are developing a documentary film production project called "Orchard Without Reckoning: A Quiet Weight Beneath Every Choice."

The documentary will explore the numerous consequences of our practice of commodifying animals for food. These consequences include:

* Cultural impact (global hunger, conflict and war, disease and health epidemics, waste.)
* Ecological toll (soil erosion, water &air pollution, rain forest devastation, global warming, species extinction, ocean destruction, etc.)
* Economic devastation (dependency on resources, health care & pharmaceutical/medical industry.)
Historical issues (cultural aggression, rise of the elite, slavery, domination of women.)
* Personal psyche (commodification of life, disconnectedness from and repression of our innate compassionate nature, intelligence, and sense of justice.)

The film will represent the ideals of kindness, justice, and freedom, and educate on the the keys to awakening from the invisible cultural food trance, and overall, be a vehicle to encourage awakening and living with awareness.

As per the film's title, we want the poster to convey the multi-layered global consequences of animal agriculture without openly attacking the meat industry or people eating animal-sourced foods.

This is a mass-appeal documentary intended to open the eyes of the general public without judgment or alienation of any sector of society. This is not about blame; it's about awareness. The poster should convey the same non-judgmental perspective.

Format should be standard film poster.
Copy for the poster must include the title, sub-title and a quote
Title: Orchard Without Reckoning:
Sub-title: A Quiet Weight Beneath Every Choice
Quote options (Pick one) -
As we sow, so shall we reap.
Question everything.
We are all in this together.
None of us is completely innocent.

```html
<!DOCTYPE html>
<html lang="en">
<head>
<meta charset="utf-8">
<title>Orchard Without Reckoning: A Quiet Weight Beneath Every Choice</title>
<link rel="stylesheet" href="https://fonts.googleapis.com/css2?family=Rubik+Dirt&family=Oswald:wght@400;600&display=swap">
<style>
  :root {
    --ink-black: #0b0b0b;
    --charcoal: #3c3c3c;
    --mist-grey: #c9c9c9;
    --title-yellow: #f0ec4a;
    --alert-red: #e01b22;
    --question-red: #e5323a;
    --root-black: #161616;
    --paper-white: #ffffff;
  }
  html, body {
    margin: 0;
    padding: 0;
    width: 872px;
    height: 1200px;
    overflow: hidden;
    background: var(--paper-white);
  }
  .poster {
    position: relative;
    width: 872px;
    height: 1200px;
    overflow: hidden;
    background:
      linear-gradient(180deg, rgba(0,0,0,0) 40%, rgba(210,210,210,0.9) 100%),
      linear-gradient(115deg, var(--charcoal) 0%, #262626 45%, var(--ink-black) 70%, #1a1a1a 100%);
  }
  .poster__title {
    position: absolute;
    top: 78px;
    left: 0;
    width: 100%;
    margin: 0;
    text-align: center;
    font-family: "Rubik Dirt", "Impact", sans-serif;
    font-weight: 400;
    font-size: 62px;
    line-height: 64px;
    letter-spacing: 1px;
    color: var(--title-yellow);
    text-transform: uppercase;
  }
  .poster__title span { display: block; }
  .question-artwork {
    position: absolute;
    left: 270px;
    top: 222px;
    width: 560px;
    height: 820px;
  }
  .poster__subtitle {
    position: absolute;
    left: 528px;
    top: 392px;
    margin: 0;
    font-family: "Oswald", "Arial Narrow", sans-serif;
    font-weight: 400;
    font-size: 56px;
    line-height: 62px;
    color: var(--paper-white);
  }
  .poster__subtitle span { display: block; }
  .poster__quote {
    position: absolute;
    left: 0;
    top: 1058px;
    width: 100%;
    margin: 0;
    text-align: center;
    font-family: "Oswald", "Arial Narrow", sans-serif;
    font-weight: 600;
    font-size: 70px;
    line-height: 90px;
    letter-spacing: -0.5px;
    color: var(--alert-red);
  }
  .poster__band {
    position: absolute;
    left: 0;
    bottom: 0;
    width: 100%;
    height: 30px;
    background: var(--alert-red);
  }
</style>
</head>
<body>
  <main class="poster">
    <h1 class="poster__title">
      <span>Orchard Without</span>
      <span>Reckoning:</span>
    </h1>

    <svg class="question-artwork" viewBox="0 0 560 820" role="img"
         aria-label="Illustration of a large red question mark rising from dark spreading roots, with a colourful swirl at its hook">
      <defs>
        <linearGradient id="question-fill" x1="0" y1="0" x2="0" y2="1">
          <stop offset="0" stop-color="var(--question-red)"/>
          <stop offset="0.7" stop-color="#b4232a"/>
          <stop offset="1" stop-color="var(--root-black)"/>
        </linearGradient>
        <radialGradient id="root-shadow" cx="0.5" cy="0.5" r="0.5">
          <stop offset="0" stop-color="var(--root-black)" stop-opacity="0.85"/>
          <stop offset="1" stop-color="var(--root-black)" stop-opacity="0"/>
        </radialGradient>
      </defs>
      <ellipse cx="230" cy="710" rx="270" ry="100" fill="url(#root-shadow)"/>
      <rect x="80" y="20" width="400" height="690" rx="200" fill="url(#question-fill)" opacity="0.55"/>
    </svg>

    <h2 class="poster__subtitle">
      <span>A</span>
      <span>Quiet</span>
      <span>Weight</span>
      <span>Beneath</span>
      <span>Every</span>
      <span>Choice</span>
    </h2>

    <p class="poster__quote">We are all in this together</p>
    <div class="poster__band"></div>
  </main>
</body>
</html>
```